Dune Loop needs some awesome stationary

Do you have what it takes to get my brand? You either do or you don't, have a crack at a design and you my just win my business.

I don't want to waste your or my time, so put your creative genius on either a business card or envelope.

I however need a package of stationary that follows the same brand. I will message you to complete the remaining should I like your first submission.

Here is what I need, have a go!

Basically I need the following for my small business based in melbourne.
- Letterhead (printer ready and MS Word)
- Business Card
- Compliments Slip
- Envelope
- Proposal Cover Page (MS Word only)
- Presentation Folder
- Harbor Tally Cards
- Student Name Tent
- Index Cards
- Tack-Pad

I am establishing the brand and it must be modern, professional but also relaxed; that is not formal and not corporate. It represents a company are leaders, but small enough to care and operate like a bunch of friends. We are bringing people and conversations back to business, and turfing out all the bureaucracy and crazy and wasteful procedures. Its about "lets talk and figure it out together and find even better ways".

Target Market(s)

Mainly companies that build software products, but Agile practices are used in many other industries (even graphic design projects)

Industry/Entity Type

Information Technology

Font styles to use
Sans Serif

Colors
3176b5
aaaaaa

Requirements
Must have
• I like curves and circles and not boxes or rectangles.
• I want a colour rich design with my brand colours, but it must be balanced.
• I want more modern than traditional, but simple modern
Should not have
• Not corporate
• Please don't waste my time if your not going to think about it.
• Don't mess with my primary logo
• Don't change my colours
• Don't overlay logo on image

```html
<!DOCTYPE html>
<html lang="en">
<head>
<meta charset="utf-8">
<title>Dune Loop — Business Card</title>
<link rel="stylesheet" href="https://fonts.googleapis.com/css2?family=Open+Sans:wght@400;600;700&display=swap">
<style>
  :root {
    --page-bg: #e8e9ea;
    --card-bg: #f1f1f1;
    --brand-blue: #2b5797;
    --brand-grey: #8a94a1;
    --ink: #2a2a2a;
    --muted: #8a8f96;
  }
  * { box-sizing: border-box; margin: 0; padding: 0; }
  html, body { width: 1200px; height: 800px; overflow: hidden; }
  body {
    background: var(--page-bg);
    font-family: "Open Sans", Arial, sans-serif;
    display: flex;
    align-items: center;
    justify-content: center;
    gap: 60px;
  }
  .card {
    position: relative;
    width: 480px;
    height: 312px;
    background: var(--card-bg);
    overflow: hidden;
  }
  .card__decor {
    position: absolute;
    inset: 0;
    width: 480px;
    height: 312px;
  }
  /* Front */
  .brand-mark {
    position: absolute;
    display: flex;
    align-items: center;
    gap: 8px;
    color: var(--brand-blue);
    font-weight: 600;
  }
  .card--front .brand-mark {
    top: 40px;
    left: 276px;
    font-size: 27px;
  }
  .brand-mark__dot {
    width: 28px;
    height: 28px;
    border-radius: 50%;
    background: var(--brand-blue);
  }
  .person {
    position: absolute;
    top: 130px;
    left: 280px;
  }
  .person__name {
    color: var(--brand-blue);
    font-size: 18px;
    font-weight: 600;
    line-height: 1.2;
  }
  .person__role {
    color: var(--ink);
    font-size: 10.5px;
    margin-top: 4px;
  }
  .contact {
    position: absolute;
    top: 196px;
    left: 280px;
    list-style: none;
    color: var(--ink);
    font-size: 13px;
    line-height: 1.5;
  }
  .contact__item {
    display: flex;
    align-items: flex-start;
    gap: 10px;
  }
  .contact__icon {
    flex: none;
    width: 11px;
    height: 11px;
    margin-top: 4px;
    fill: var(--brand-blue);
  }
  /* Back */
  .card--back .brand-mark {
    top: 60px;
    left: 240px;
    width: 230px;
    flex-direction: column;
    gap: 12px;
    font-size: 34px;
  }
  .card--back .brand-mark__dot {
    width: 62px;
    height: 62px;
  }
  .company {
    position: absolute;
    top: 200px;
    left: 240px;
    width: 230px;
    text-align: center;
    color: var(--muted);
    font-size: 12.5px;
    line-height: 1.5;
  }
  .company__name { font-weight: 700; }
  .company__phone strong { font-weight: 700; }
</style>
</head>
<body>
  <svg width="0" height="0" style="position:absolute">
    <defs>
      <linearGradient id="decor-fill" x1="0" y1="0" x2="0" y2="1">
        <stop offset="0" stop-color="#2b5797"/>
        <stop offset="0.55" stop-color="#3a5f94"/>
        <stop offset="1" stop-color="#8a94a1"/>
      </linearGradient>
    </defs>
  </svg>

  <section class="card card--front">
    <svg class="card__decor" viewBox="0 0 480 312" role="img" aria-label="Brand curve artwork in blue and grey">
      <path d="M0 0 H250 C 282 90, 262 210, 165 312 H0 Z" fill="url(#decor-fill)"/>
    </svg>
    <div class="brand-mark"><span class="brand-mark__dot"></span><span>Dune Loop</span></div>
    <div class="person">
      <p class="person__name">Owen Calder</p>
      <p class="person__role">CEO, Professional Agile Trainer</p>
    </div>
    <ul class="contact">
      <li class="contact__item">
        <svg class="contact__icon" viewBox="0 0 12 12"><path d="M6 0a4 4 0 0 0-4 4c0 3 4 8 4 8s4-5 4-8a4 4 0 0 0-4-4zm0 5.6a1.6 1.6 0 1 1 0-3.2 1.6 1.6 0 0 1 0 3.2z"/></svg>
        <span>PO Box 4410, Ridgeview<br>North, VIC 3199, Australia</span>
      </li>
      <li class="contact__item">
        <svg class="contact__icon" viewBox="0 0 12 12"><circle cx="6" cy="6" r="6"/><rect x="3" y="5.2" width="6" height="1.6" fill="#f1f1f1"/></svg>
        <span>owen@duneloop.com.au</span>
      </li>
      <li class="contact__item">
        <svg class="contact__icon" viewBox="0 0 12 12"><path d="M2.4 0.5 4.3 2.7 3.3 4.2c.8 1.8 2.3 3.3 4.5 4.5l1.5-1 2.2 1.9-1.3 1.9C5 11.3.7 7 .5 1.8z"/></svg>
        <span>+61 400 555 019</span>
      </li>
    </ul>
  </section>

  <section class="card card--back">
    <svg class="card__decor" viewBox="0 0 480 312" role="img" aria-label="Brand curve artwork in blue and grey">
      <path d="M0 0 H250 C 282 90, 262 210, 165 312 H0 Z" fill="url(#decor-fill)"/>
    </svg>
    <div class="brand-mark"><span class="brand-mark__dot"></span><span>Dune Loop</span></div>
    <div class="company">
      <p class="company__name">Dune Loop Pty Ltd</p>
      <p class="company__phone">Phone <strong>1300DUNES</strong></p>
      <p class="company__web">www.duneloop.com.au</p>
    </div>
  </section>
</body>
</html>
```